Physical Large Banner For Corporate Event

Hi, we would like a large banner designed for a corporate event using adobe illustrator/pdf. The size of the banner must be 2000 (h)x800 (w) mm to fit with the printing requirements (please visit https://www.inkvaleprints.com/products/48/banner-stands and see the guidelines for size for a standard banner)

Our organisation holds events for students to find out more on top careers such as Investment Banking & Law. The banner design can be fairly simple but bold using the same themes and colours on our website www.brightlanefutures.co.uk. We can provide imagery of our logo for use/other pictures requested such as those for students/cityscapes etc.

The only text on the banner should be our web address at the bottom (www.brightlanefutures.co.uk) and a line that says "A Head Start in the City, We bring the internship to you..." like in our website homepage.

Target Market(s)

Students & Graduate Recruiters

Industry/Entity Type

Education

Requirements
Must have
• Website address
• Cool imagery
Should not have
• Too much clutter, clean and simple pleaseE

```html
<!DOCTYPE html>
<html lang="en">
<head>
<meta charset="utf-8">
<title>BrightLane Banner Proposal</title>
<link rel="stylesheet" href="https://fonts.googleapis.com/css2?family=Arimo:wght@400&family=Tinos:wght@400&family=Raleway:wght@100;400&display=swap">
<style>
  :root {
    --sheet: #ffffff;
    --sky-deep: #0b3fa8;
    --sky-mid: #2f7fe0;
    --haze: #f4f8fc;
    --cloud-blue: #3aa6e8;
    --cloud-light: #8fd0f2;
    --brand-grey: #6e6e70;
    --tagline-outline: #7cc6ee;
    --numeral: #cfcfcf;
    --rule: #a9c3d2;
    --caption: #8a8a8a;
    --white: #ffffff;
  }
  * { margin: 0; padding: 0; box-sizing: border-box; }
  html, body { width: 1200px; height: 849px; overflow: hidden; background: var(--sheet); }
  .sheet { position: relative; width: 1200px; height: 849px; background: var(--sheet); }

  .banner {
    position: absolute;
    top: 51px;
    width: 260px;
    height: 653px;
    overflow: hidden;
  }
  .banner--one { left: 170px; }
  .banner--two { left: 661px; }

  .banner__sky {
    position: absolute; inset: 0;
    background: linear-gradient(180deg,
      var(--sky-deep) 0%,
      var(--sky-mid) 12%,
      #9cc4ee 21%,
      var(--haze) 28%,
      var(--haze) 40%,
      var(--cloud-light) 50%,
      #5db9ec 62%,
      var(--cloud-blue) 78%,
      #2f9de4 100%);
  }

  .brand-mark {
    position: absolute;
    background: var(--brand-grey);
  }
  .banner--one .brand-mark { left: 95px; top: 120px; width: 70px; height: 70px; }
  .banner--two .brand-mark { left: 76px; top: 122px; width: 44px; height: 44px; }

  .brand {
    position: absolute;
    font-family: "Tinos", "Times New Roman", serif;
    font-weight: 400;
    color: var(--brand-grey);
    white-space: nowrap;
    line-height: 1;
  }
  .banner--one .brand { left: 0; right: 0; top: 210px; text-align: center; font-size: 48px; }
  .banner--two .brand { left: 0; width: 196px; top: 178px; text-align: center; font-size: 32px; }

  .tagline {
    position: absolute;
    left: 9px; top: 353px;
    font-family: "Arimo", Arial, sans-serif;
    font-size: 15px; line-height: 18px;
    color: var(--white);
  }

  .web {
    position: absolute;
    font-family: "Arimo", Arial, sans-serif;
    color: var(--white);
    white-space: nowrap;
    line-height: 1;
  }
  .banner--one .web { left: 0; right: 0; top: 613px; text-align: center; font-size: 17.5px; }
  .banner--two .web { left: 8px; top: 619px; font-size: 12px; }

  .tagline-vertical {
    position: absolute;
    left: 258px; top: 556px;
    width: 600px; height: 80px;
    transform-origin: 0 100%;
    transform: rotate(-90deg);
    font-family: "Arimo", Arial, sans-serif;
    font-size: 40px; line-height: 39px;
    color: var(--white);
    -webkit-text-stroke: 1px var(--tagline-outline);
    white-space: nowrap;
  }

  .numeral {
    position: absolute;
    top: 558px;
    font-family: "Raleway", sans-serif;
    font-weight: 100;
    font-size: 175px; line-height: 1;
    color: var(--numeral);
  }
  .numeral--one { left: 436px; }
  .numeral--two { left: 948px; }

  .footer-rule {
    position: absolute; left: 0; top: 755px;
    width: 1200px; height: 3px;
    background: var(--rule);
  }
  .caption {
    position: absolute; right: 10px; top: 783px;
    font-family: "Raleway", sans-serif;
    font-size: 11px; letter-spacing: 7px;
    color: var(--caption);
  }
</style>
</head>
<body>
<main class="sheet">

  <section class="banner banner--one">
    <div class="banner__sky" role="img" aria-label="Photograph of a deep blue sky fading to white above a field of white clouds"></div>
    <div class="brand-mark"></div>
    <div class="brand">BrightLane</div>
    <p class="tagline">A Head Start in the City<br>We bring the internship to you...</p>
    <p class="web">www.brightlanefutures.co.uk</p>
  </section>
  <div class="numeral numeral--one">1</div>

  <section class="banner banner--two">
    <div class="banner__sky" role="img" aria-label="Photograph of a deep blue sky fading to white above a field of white clouds"></div>
    <div class="brand-mark"></div>
    <div class="brand">BrightLane</div>
    <p class="web">www.brightlanefutures.co.uk</p>
    <p class="tagline-vertical">A Head Start in the City<br>We bring the internship to you...</p>
  </section>
  <div class="numeral numeral--two">2</div>

  <div class="footer-rule"></div>
  <p class="caption">PROPOSAL FOR BRIGHTLANE BANNER</p>

</main>
</body>
</html>
```